Wordpress Design Project

Need a page like this but with your own personal twist

I will provide you the iframed form on 2nd page

http://www.plumcoverdeals.example/index4421.php?subid=3092647

Requirements
Must have
• Article with link out
must pass zipcode to iframed form on 2nd page.

Must provide css for form pages.

```html
<!DOCTYPE html>
<html lang="en">
<head>
<meta charset="utf-8">
<title>Plumcover Auto – Save Big on Your Auto Insurance</title>
<link rel="stylesheet" href="https://fonts.googleapis.com/css2?family=Anton&family=Oswald:wght@700&family=Yanone+Kaffeesatz:wght@400;500&family=Open+Sans:wght@400;600&display=swap">
<style>
  :root {
    --green: #8cc63f;
    --green-dark: #76ad2c;
    --charcoal: #3b3d40;
    --red: #d7141a;
    --ink: #333333;
    --text: #222222;
    --muted: #8a8a8a;
    --line: #c9c9c9;
    --panel: #f1f1f1;
    --footer: #3a3a3a;
    --link: #3b5998;
  }
  * { box-sizing: border-box; margin: 0; padding: 0; }
  html, body { width: 1200px; height: 1181px; overflow: hidden; }
  body {
    position: relative;
    background: repeating-linear-gradient(135deg, #f4f4f4 0 2px, #fbfbfb 2px 5px);
    font-family: "Open Sans", Arial, sans-serif;
    color: var(--text);
  }
  .abs { position: absolute; }

  .header-bg { left: 0; top: 0; width: 1200px; height: 242px; background: linear-gradient(#eeeeee, #ffffff 60%); }
  .brand { left: 154px; top: 34px; font-family: "Oswald", sans-serif; font-weight: 700; font-size: 38px; color: var(--ink); letter-spacing: -0.5px; }
  .tagline { left: 154px; top: 80px; font-size: 13.5px; letter-spacing: 2.2px; color: #555; }
  .call { right: 183px; top: 16px; font-family: "Yanone Kaffeesatz", sans-serif; font-weight: 500; font-size: 28px; color: var(--ink); }
  .call span { color: var(--red); }

  .hero { left: 152px; top: 130px; width: 893px; height: 112px; background: #fff; border: 1px solid #d6d6d6; border-bottom: none; }
  .save { left: 162px; top: 126px; font-family: "Anton", sans-serif; font-size: 60px; color: var(--red); line-height: 1.1; }
  .offer { left: 162px; top: 192px; font-family: "Yanone Kaffeesatz", sans-serif; font-weight: 500; font-size: 29px; color: var(--ink); }
  .offer b { font-family: "Anton", sans-serif; font-weight: 400; font-size: 33px; }
  .car { left: 632px; top: 53px; width: 443px; height: 190px; border-radius: 90px 120px 20px 30px; background: radial-gradient(ellipse at 55% 55%, #d2d4d6, #9ea2a6 70%, rgba(255,255,255,0) 72%); }

  .band { left: 0; top: 242px; width: 1200px; height: 124px; background: linear-gradient(#f3f3f3, #dedede 50%, #eeeeee); }
  .steps { left: 130px; top: 242px; }
  .step-label { font-family: "Anton", sans-serif; font-size: 58px; fill: #fff; }

  .main { left: 152px; top: 366px; width: 893px; height: 750px; background: #fff; border: 1px solid #d6d6d6; border-top: none; }
  .fold { top: 366px; }

  .step-text { top: 378px; font-size: 27px; line-height: 33px; color: var(--ink); text-align: center; }
  .step-text em { font-style: normal; color: var(--red); }

  .zip-box { left: 178px; top: 459px; width: 838px; height: 82px; background: var(--panel); border: 1px solid var(--line); border-radius: 3px; }
  .zip-label { left: 213px; top: 485px; font-size: 21px; color: #444; }
  .zip-input { left: 471px; top: 482px; width: 183px; height: 36px; background: #fff; border: 1px solid #bdbdbd; border-radius: 4px; }
  .continue { left: 668px; top: 482px; width: 147px; height: 36px; border-radius: 4px; background: linear-gradient(#e8262b, #b50d12); color: #fff; font-family: Arial, sans-serif; font-weight: 700; font-size: 22px; display: flex; align-items: center; justify-content: center; gap: 8px; border: 1px solid #9a0a0e; }
  .badge { left: 862px; top: 477px; width: 128px; height: 46px; border-radius: 4px; background: #d8d8d8; }
  .badge-note { left: 900px; top: 522px; font-size: 9px; color: #666; }

  .article-title { left: 182px; top: 561px; font-family: "Yanone Kaffeesatz", sans-serif; font-weight: 500; font-size: 28px; color: var(--text); }
  .article { left: 182px; top: 605px; width: 531px; font-family: Arial, sans-serif; font-size: 14.6px; line-height: 19px; color: var(--text); text-align: justify; }
  .article p { margin-bottom: 19px; }
  .article a { color: var(--text); text-decoration: none; }

  .reviews-title { left: 749px; top: 560px; font-family: "Yanone Kaffeesatz", sans-serif; font-weight: 500; font-size: 28px; color: var(--text); }
  .bubble { left: 749px; top: 608px; }
  .quote { left: 766px; top: 625px; width: 234px; font-family: Arial, sans-serif; font-style: italic; font-size: 14.4px; line-height: 17.5px; color: #444; text-align: center; }
  .visitor { left: 888px; top: 778px; font-family: Arial, sans-serif; font-style: italic; font-size: 15px; color: var(--red); }

  .social { left: 749px; top: 826px; width: 267px; height: 270px; border: 1px solid #bdbdbd; background: #fff; font-family: Arial, sans-serif; }
  .social-head { height: 28px; background: #f0f0f0; border-bottom: 1px solid #d4d4d4; font-size: 11.5px; font-weight: 700; padding: 7px 9px; color: #222; }
  .social-name { margin: 9px 0 0 5px; font-size: 14px; color: var(--link); }
  .social-name small { font-size: 12px; }
  .social-like { margin: 2px 0 0 5px; font-size: 10px; color: #333; padding-bottom: 7px; border-bottom: 1px solid #e3e3e3; width: 250px; }
  .social-like span { color: var(--link); }
  .fans { margin: 7px 0 0 9px; font-size: 10px; color: #333; }
  .fan-grid { display: grid; grid-template-columns: repeat(5, 44px); column-gap: 5px; row-gap: 6px; margin: 4px 0 0 9px; }
  .fan { text-align: center; font-size: 8.5px; color: #6d84b4; }
  .fan-photo { width: 44px; height: 44px; margin-bottom: 2px; }
  .plugin { margin: 8px 0 0 9px; font-size: 9px; color: #555; display: flex; align-items: center; gap: 4px; }
  .plugin i { width: 11px; height: 11px; background: var(--link); display: inline-block; }

  .footer { left: 0; top: 1120px; width: 1200px; height: 61px; background: var(--footer); font-size: 13px; color: #e4e4e4; }
  .footer-links { left: 165px; top: 8px; }
  .footer-links span { margin: 0 9px; }
  .copyright { left: 165px; top: 33px; font-size: 11px; color: #cfcfcf; }
</style>
</head>
<body>
  <div class="abs header-bg"></div>
  <div class="abs brand">Plumcover Auto</div>
  <div class="abs tagline">YOUR PUNCH LINE GOSE HERE</div>
  <div class="abs call">Call us: <span>555-014-2290</span></div>

  <div class="abs hero"></div>
  <div class="abs save">Save Big!</div>
  <div class="abs offer">on Your Auto Insurance as low as <b>$7/WEEK</b></div>
  <div class="abs car" role="img" aria-label="Silver hatchback car, side view"></div>

  <div class="abs band"></div>
  <svg class="abs steps" width="941" height="124" viewBox="0 0 941 124">
    <polygon points="0,0 290,0 330,62 290,124 0,124" fill="var(--green)"/>
    <polygon points="302,0 652,0 692,62 652,124 302,124 342,62" fill="var(--charcoal)"/>
    <polygon points="664,0 941,0 941,124 664,124 704,62" fill="var(--green)"/>
    <polyline points="10,10 276,10 309,62 276,114 10,114" fill="none" stroke="rgba(255,255,255,0.25)"/>
    <polyline points="330,10 638,10 671,62 638,114 330,114" fill="none" stroke="rgba(255,255,255,0.15)"/>
    <polyline points="700,10 931,10 931,114 700,114" fill="none" stroke="rgba(255,255,255,0.25)"/>
    <text class="step-label" x="123" y="86" text-anchor="middle">Step 1</text>
    <text class="step-label" x="482" y="86" text-anchor="middle">Step 2</text>
    <text class="step-label" x="808" y="86" text-anchor="middle">Step 3</text>
  </svg>

  <div class="abs main"></div>
  <svg class="abs fold" style="left:130px" width="22" height="22"><polygon points="0,0 22,0 22,22" fill="#3a3a3a"/></svg>
  <svg class="abs fold" style="left:1045px" width="26" height="22"><polygon points="0,0 26,0 0,22" fill="#3a3a3a"/></svg>

  <div class="abs step-text" style="left:175px;width:200px">Enter your zip code.</div>
  <div class="abs step-text" style="left:455px;width:300px">Fill out your vehicle &amp; driver information.</div>
  <div class="abs step-text" style="left:820px;width:210px">Compare rates &amp; <em>SAVE!</em></div>

  <svg class="abs" style="left:372px;top:410px" width="105" height="65" viewBox="0 0 105 65">
    <path d="M4,50 C20,8 68,2 86,36" fill="none" stroke="var(--red)" stroke-width="9" stroke-linecap="round"/>
    <polygon points="70,38 102,34 92,64" fill="var(--red)"/>
  </svg>

  <div class="abs zip-box"></div>
  <div class="abs zip-label">Enter your Zip coad here</div>
  <div class="abs zip-input"></div>
  <div class="abs continue">Continue
    <svg width="16" height="16" viewBox="0 0 16 16"><circle cx="8" cy="8" r="8" fill="#fff"/><polygon points="6,4 11,8 6,12" fill="#c0121a"/></svg>
  </div>
  <div class="abs badge" role="img" aria-label="Security verification badge"></div>
  <div class="abs badge-note">Click to Verify</div>

  <h1 class="abs article-title">Suspendisse quis placerat massa, porta luctus dolor</h1>
  <div class="abs article">
    <p>Lorem ipsum dolor sit amet, consectetur adipiscing elit. Duis nec ultricies eros. Aliquam nec enim odio. Proin semper sem sollicitudin massa adipiscing, nec egestas tellus egestas. Duis vel erat eget augue iaculis fermentum. Praesent sagittis mauris ut fringilla tempor. Nullam viverra est sem, eu tincidunt quam rutrum eu. Proin ullamcorper arcu consectetur, tincidunt ante id, eleifend nisi. Donec fringilla mi eget purus gravida, id vulputate velit bibendum. In non turpis tincidunt neque imperdiet porta. Donec vel pellentesque eros. Phasellus fringilla scelerisque nisl. Etiam cursus risus ac sem pulvinar rhoncus. Fusce ornare viverra lectus quis fermentum. Fusce porta imperdiet sodales. Lorem ipsum dolor sit amet, consectetur adipiscing elit. Mauris tempus laoreet diam, a aliquet dolor faucibus sit amet.</p>
    <p>Suspendisse quis placerat massa, porta luctus dolor. In in tellus massa. Mauris egestas nunc non blandit fringilla. Duis tincidunt feugiat mauris ut facilisis. Fusce elementum quam at dui luctus, accumsan hendrerit lorem tempor. Pellentesque consequat ultricies lectus, posuere volutpat lacus ultrices sit amet. Cras varius augue sapien, et interdum tellus rutrum vitae. Donec quis lacus dignissim sem scelerisque laoreet. Fusce suscipit ultrices scelerisque. Proin fermentum dui tempus aliquam auctor. Ut nec est et velit euismod rhoncus vel eget erat. Phasellus lobortis justo massa, et interdum elit vehicula imperdiet.</p>
    <p>Fusce ornare viverra lectus quis fermentum. Fusce porta imperdiet sodales. Lorem ipsum dolor sit amet, consectetur adipiscing elit. Mauris tempus laoreet diam, a <a href="http://www.plumcoverdeals.example/index4421.php?subid=3092647">aliquet dolor faucibus sit amet.</a></p>
  </div>

  <h2 class="abs reviews-title">Visitor Reviews</h2>
  <svg class="abs bubble" width="267" height="158" viewBox="0 0 267 158">
    <path d="M14,1 H253 A13,13 0 0 1 266,14 V127 A13,13 0 0 1 253,140 H236 L226,156 L220,140 H14 A13,13 0 0 1 1,127 V14 A13,13 0 0 1 14,1 Z" fill="#ebebeb" stroke="#bdbdbd"/>
  </svg>
  <div class="abs quote">Nunc non sapien a leo tempus hendrerit. Quisque placerat convallis dui id varius. Mauris justo enim, tristique in pulvinar ut, dignissim at lacus. Proin sagittis odio porta enim malesuada, eget auctor augue lacinia.</div>
  <div class="abs visitor">Visitor Name Here</div>

  <div class="abs social">
    <div class="social-head">Find us on Friendpage</div>
    <div class="social-name">Plumcover Auto <small>on Friendpage</small></div>
    <div class="social-like">You like this. <span>Unlike</span></div>
    <div class="fans">Ravin's Blog has 17 fans</div>
    <div class="fan-grid">
      <div class="fan"><div class="fan-photo" role="img" aria-label="Fan profile photo" style="background:#6b4a3a"></div>Tomas</div>
      <div class="fan"><div class="fan-photo" role="img" aria-label="Fan profile photo" style="background:#7d6a5c"></div>Milo</div>
      <div class="fan"><div class="fan-photo" role="img" aria-label="Fan profile photo" style="background:#8a7560"></div>Ravin</div>
      <div class="fan"><div class="fan-photo" role="img" aria-label="Fan profile photo" style="background:#7fb7b0"></div>Arlo</div>
      <div class="fan"><div class="fan-photo" role="img" aria-label="Fan profile photo" style="background:#6e4434"></div>Tomas</div>
      <div class="fan"><div class="fan-photo" role="img" aria-label="Fan profile photo" style="background:#9a7b6a"></div>Ravin</div>
      <div class="fan"><div class="fan-photo" role="img" aria-label="Fan profile photo" style="background:#8c8f6c"></div>Devin</div>
      <div class="fan"><div class="fan-photo" role="img" aria-label="Fan profile photo" style="background:#a98a66"></div>Kiran</div>
      <div class="fan"><div class="fan-photo" role="img" aria-label="Fan profile photo" style="background:#5d5452"></div>Omar</div>
      <div class="fan"><div class="fan-photo" role="img" aria-label="Fan profile photo" style="background:#c4a79a"></div>Ravin</div>
    </div>
    <div class="plugin"><i></i>Friendpage social plugin</div>
  </div>

  <footer class="abs footer">
    <div class="abs footer-links">Home<span>|</span>Privacy Policy<span>|</span>Terms of Use</div>
    <div class="abs copyright">Copyright 2013 plumcoverdeals.example All Rights Reserved.</div>
  </footer>
</body>
</html>
```